依頼詳細
新会社の名刺デザインをお願いします。
こちらでデザインして頂いたロゴを使用し、爽やかで誰からも好かれるデザインを希望します。
若い会社ですので、多少の遊び心も欲しいです。
よろしくお願いします。
記載項目
表面;会社名、役職、名前、住所、電話、ファックス、携帯、メール、webアドレス
裏面;各項目の英字。別の物で、何かご提案があれば。
希望イメージ
シンプル 複雑
単色 カラフル
暗い 明るい
日常 高級
遊び心 厳粛
未来的 伝統的
女性的 男性的
希望する色
青系、水色系
納品ファイル
• 高解像度JPG (.jpg)
• イラストレーター形式 (.ai)
• PNG形式 (.png)
補足説明
■ 選んだ理由

シンプルで受け入れやすいデザインでした。

■ 提案者全員のお礼・コメント

皆様趣向を凝らしたご提案ありがとうございました。
また、機会があればよろしくお願い致します。

```html
<!DOCTYPE html>
<html lang="ja">
<head>
<meta charset="utf-8">
<title>Business Card – Front &amp; Back</title>
<link rel="stylesheet" href="https://fonts.googleapis.com/css2?family=Noto+Sans+JP:wght@400;500;700&display=swap">
<style>
  :root{
    --board:#d9d9d9;
    --card:#ffffff;
    --ink:#333333;
    --ink-soft:#555555;
    --brand:#1f9ad6;
    --sky:#a9d9f2;
    --sky-pale:#e3f3fc;
  }
  *{box-sizing:border-box;margin:0;padding:0}
  html,body{width:798px;height:1200px;overflow:hidden}
  body{background:var(--board);font-family:"Noto Sans JP",sans-serif;color:var(--ink);position:relative}
  .side-label{position:absolute;left:48px;font-size:20px;color:var(--ink-soft)}
  .side-label.front{top:68px}
  .side-label.back{top:622px}
  .card{position:absolute;left:48px;width:718px;height:436px;background:var(--card);overflow:hidden;box-shadow:0 2px 6px rgba(0,0,0,.15)}
  .card.front{top:110px}
  .card.back{top:664px}
  .sky-art{position:absolute;left:300px;top:90px;width:418px;height:346px;
    background:radial-gradient(ellipse 75% 70% at 80% 60%,var(--sky) 0%,var(--sky-pale) 55%,rgba(255,255,255,0) 100%)}
  .content{position:relative}
  .brand{position:absolute;left:40px;top:36px;display:flex;align-items:center;gap:12px}
  .brand-dot{width:20px;height:20px;border-radius:50%;background:var(--brand)}
  .brand-name{font-size:54px;font-weight:700;color:var(--brand);letter-spacing:2px;line-height:1}
  .url{position:absolute;left:276px;top:80px;font-size:18px;font-weight:700;color:var(--ink)}
  .person{position:absolute;left:172px}
  .front .person{top:140px}
  .back .person{top:150px}
  .role{font-size:17px}
  .name{font-size:40px;font-weight:500;line-height:1.2;letter-spacing:2px}
  .name small{font-size:16px;letter-spacing:0;margin-left:8px}
  .back .name{font-size:44px;letter-spacing:0}
  .contact{display:flex;align-items:center;gap:8px;font-size:18px;margin-top:4px}
  .company{position:absolute;left:40px;top:300px}
  .company-name{font-size:20px;font-weight:500;margin-bottom:6px}
  .company .contact{margin-top:3px;font-size:17px}
  .icon{width:18px;height:18px;flex:none}
  .gap{margin-left:10px}
</style>
</head>
<body>

<p class="side-label front">Front</p>
<section class="card front">
  <div class="sky-art" role="img" aria-label="Sky-blue sweeping band with faint airplane silhouettes flying upward"></div>

  <div class="brand"><span class="brand-name">SCT</span><span class="brand-dot"></span></div>
  <p class="url">http://www.example.com</p>

  <div class="person">
    <p class="role">代表取締役</p>
    <p class="name">川村 一郎<small>Ichiro Kawamura</small></p>
    <p class="contact"><svg class="icon" viewBox="0 0 18 18"><rect width="18" height="18" rx="3" fill="var(--brand)"/><rect x="6" y="3" width="6" height="12" rx="1" fill="#fff"/></svg>090-1234-5678</p>
  </div>

  <div class="company">
    <p class="company-name">株式会社 Skyline Creative Technologies</p>
    <p class="contact"><svg class="icon" viewBox="0 0 18 18"><rect width="18" height="18" rx="3" fill="var(--brand)"/><path d="M9 3a4 4 0 0 1 4 4c0 3-4 8-4 8S5 10 5 7a4 4 0 0 1 4-4z" fill="#fff"/></svg>107-0000 東京都港区青山5-6-78 青空ビル3F</p>
    <p class="contact"><svg class="icon" viewBox="0 0 18 18"><rect width="18" height="18" rx="3" fill="var(--brand)"/><path d="M5 4h3l1 3-2 1a7 7 0 0 0 3 3l1-2 3 1v3a1 1 0 0 1-1 1A10 10 0 0 1 4 5a1 1 0 0 1 1-1z" fill="#fff"/></svg>03-1111-2222
      <svg class="icon gap" viewBox="0 0 18 18"><rect width="18" height="18" rx="3" fill="var(--brand)"/><rect x="4" y="7" width="10" height="6" fill="#fff"/><rect x="6" y="4" width="6" height="3" fill="#fff"/></svg>03-1111-2223</p>
    <p class="contact"><svg class="icon" viewBox="0 0 18 18"><rect width="18" height="18" rx="3" fill="var(--brand)"/><rect x="3" y="5" width="12" height="8" fill="#fff"/><path d="M3 5l6 5 6-5" fill="none" stroke="var(--brand)" stroke-width="1.2"/></svg>info@example.com</p>
  </div>
</section>

<p class="side-label back">Back</p>
<section class="card back">
  <div class="sky-art" role="img" aria-label="Sky-blue sweeping band with faint airplane silhouettes flying upward"></div>

  <div class="brand"><span class="brand-name">SCT</span><span class="brand-dot"></span></div>

  <div class="person">
    <p class="role">CEO</p>
    <p class="name">Ichiro Kawamura</p>
    <p class="contact"><svg class="icon" viewBox="0 0 18 18"><rect width="18" height="18" rx="3" fill="var(--brand)"/><rect x="6" y="3" width="6" height="12" rx="1" fill="#fff"/></svg>090-1234-5678</p>
  </div>

  <div class="company">
    <p class="company-name">Skyline Creative Technologies Co., Ltd.</p>
    <p class="contact"><svg class="icon" viewBox="0 0 18 18"><rect width="18" height="18" rx="3" fill="var(--brand)"/><path d="M9 3a4 4 0 0 1 4 4c0 3-4 8-4 8S5 10 5 7a4 4 0 0 1 4-4z" fill="#fff"/></svg>Aozora Bld 3F,5-6-78,Aoyama,Minato-ku,Tokyo,107-0000, Japan</p>
    <p class="contact"><svg class="icon" viewBox="0 0 18 18"><rect width="18" height="18" rx="3" fill="var(--brand)"/><path d="M5 4h3l1 3-2 1a7 7 0 0 0 3 3l1-2 3 1v3a1 1 0 0 1-1 1A10 10 0 0 1 4 5a1 1 0 0 1 1-1z" fill="#fff"/></svg>+81-3-1111-2222
      <svg class="icon gap" viewBox="0 0 18 18"><rect width="18" height="18" rx="3" fill="var(--brand)"/><rect x="4" y="7" width="10" height="6" fill="#fff"/><rect x="6" y="4" width="6" height="3" fill="#fff"/></svg>+81-3-1111-2223</p>
    <p class="contact"><svg class="icon" viewBox="0 0 18 18"><rect width="18" height="18" rx="3" fill="var(--brand)"/><rect x="3" y="5" width="12" height="8" fill="#fff"/><path d="M3 5l6 5 6-5" fill="none" stroke="var(--brand)" stroke-width="1.2"/></svg>info@example.com</p>
  </div>
</section>

</body>
</html>
```